Hawaiian fusion restaurant seeks new website design for upcoming 15th anniversary

We currently have a website-- kavoramesaplate.com-- but it's boring and we really want something exciting and fresh.

Coded - Design and coding required

1 page

Serif
Sans Serif

00AB8E
00BBA5
67D7C9
C6EFE9
E9F9F6
59FF00
82FF00
B8FF75
E3FFCB
F4FFEA
F0912C
F2A743
F7CA91
FBE8D2
FDF5EE

```html
<!DOCTYPE html>
<html lang="en">
<head>
<meta charset="utf-8">
<title>Kavora Mesa Grill</title>
<link rel="stylesheet" href="https://fonts.googleapis.com/css2?family=Kanit:wght@400;500;600&family=Montserrat:wght@400;500;600;700&display=swap">
<style>
:root{
  --orange:#F0912C;
  --orange-deep:#E8801E;
  --cream:#FDF5EE;
  --ink:#141414;
  --muted:#9a9a9a;
  --white:#ffffff;
  --gold:#F7B500;
  --field:#E4E4E4;
  --night:#1d1712;
}
*{margin:0;padding:0;box-sizing:border-box}
html,body{width:1200px;height:4286px;overflow:hidden}
body{position:relative;background:var(--white);font-family:'Montserrat',sans-serif;color:var(--ink)}
.abs{position:absolute}
.photo{position:absolute}
.shadow{box-shadow:0 4px 12px rgba(0,0,0,.35)}

/* hero */
.hero{position:absolute;left:0;top:0;width:1200px;height:676px;background:radial-gradient(ellipse at 50% 55%,#6b4a35 0%,#3a2a22 45%,#1d1a17 100%)}
.hero-shade{position:absolute;inset:0;background:linear-gradient(180deg,rgba(0,0,0,.35),rgba(0,0,0,.1) 50%,rgba(0,0,0,.35))}
.brand{position:absolute;left:38px;top:30px;display:flex;align-items:center;gap:10px}
.brand-dot{width:26px;height:26px;border-radius:50%;background:var(--orange)}
.brand-name{font-family:'Kanit',sans-serif;font-weight:500;font-size:26px;color:var(--white)}
.nav{position:absolute;right:34px;top:52px;display:flex;gap:26px;font-family:'Kanit',sans-serif;font-size:30px;color:var(--white)}
.hero-kicker{position:absolute;left:0;width:1200px;top:250px;text-align:center;font-family:'Kanit',sans-serif;font-size:25px;letter-spacing:2px;color:var(--white)}
.hero-kicker span{position:relative;padding:0 6px}
.hero-kicker span::before,.hero-kicker span::after{content:"";position:absolute;top:50%;width:170px;height:2px;background:var(--white)}
.hero-kicker span::before{right:100%}
.hero-kicker span::after{left:100%}
.hero-title{position:absolute;left:0;width:1200px;top:282px;text-align:center;font-family:'Kanit',sans-serif;font-weight:500;font-size:52px;line-height:68px;color:var(--white)}

/* welcome */
.welcome-band{position:absolute;left:0;top:676px;width:1200px;height:540px;background:var(--cream)}
.eyebrow{font-weight:700;font-size:19px;letter-spacing:2.5px;color:var(--orange)}
.welcome-title{position:absolute;left:105px;top:752px;font-weight:500;font-size:48px;line-height:60px;letter-spacing:3px}
.welcome-title em{font-style:normal;color:var(--orange);font-weight:600}
.welcome-text{position:absolute;left:105px;top:874px;width:585px;font-size:15.5px;line-height:21.5px}
.btn-solid{position:absolute;background:var(--orange);color:var(--white);font-weight:700;font-size:15px;display:flex;align-items:center;justify-content:center}
.btn-line{position:absolute;border:2px solid var(--orange);color:var(--orange);font-weight:600;font-size:14px;display:flex;align-items:center;justify-content:center;background:transparent}

/* menu */
.menu-head{position:absolute;width:300px;text-align:center}
.menu-head small{display:block;font-weight:600;font-size:15px;color:var(--orange)}
.menu-head h2{font-weight:700;font-size:31px;letter-spacing:3px;line-height:36px}
.dish{position:absolute;width:320px}
.dish h3{display:flex;justify-content:space-between;font-weight:500;font-size:19px}
.dish p{margin-top:6px;font-size:11.5px;line-height:16px;color:var(--muted);width:300px}

/* visit */
.visit-title{position:absolute;right:589px;top:2026px;text-align:right;font-family:'Kanit',sans-serif;font-weight:500;font-size:46px;line-height:60px}
.visit-lines{position:absolute;right:589px;text-align:right;font-size:19px}

/* booking */
.booking{position:absolute;left:0;top:2594px;width:1200px;height:556px;background:linear-gradient(180deg,#2b221c,#15110e)}
.booking-kicker{position:absolute;left:0;width:1200px;top:2672px;text-align:center;font-weight:600;font-size:23px;letter-spacing:2.5px;color:var(--orange)}
.booking-kicker span{position:relative;padding:0 4px}
.booking-kicker span::before,.booking-kicker span::after{content:"";position:absolute;top:50%;width:80px;height:1.5px;background:var(--orange)}
.booking-kicker span::before{right:100%}
.booking-kicker span::after{left:100%}
.booking-title{position:absolute;left:0;width:1200px;top:2718px;text-align:center;font-weight:400;font-size:60px;letter-spacing:4px;color:var(--white)}
.select{position:absolute;top:2840px;width:208px;height:34px;border-bottom:1.5px solid #cfcfcf;color:var(--white);font-size:19px;padding-left:18px;display:flex;align-items:center}
.select svg{position:absolute;right:14px;top:12px}
.offer-bar{position:absolute;left:0;top:3062px;width:1200px;height:38px;background:var(--gold)}
.offer-text{position:absolute;left:196px;top:3066px;font-size:25px;color:var(--ink)}
.offer-text strong{font-weight:600}
.badge{position:absolute;left:83px;top:3046px;font-family:'Kanit',sans-serif;font-weight:600;color:var(--white);line-height:1}
.badge b{display:block;font-size:38px}
.badge i{display:block;font-style:normal;font-size:17px}

/* catering */
.catering-title{position:absolute;left:602px;top:3282px;font-family:'Kanit',sans-serif;font-weight:600;font-size:54px}
.catering-text{position:absolute;left:602px;top:3362px;width:510px;font-size:19.5px;line-height:28.5px}
.field{position:absolute;left:602px;width:500px;background:var(--field);font-weight:600;font-size:14px;padding:6px 10px}

/* footer */
.footer{position:absolute;left:0;top:3899px;width:1200px;height:387px;background:#000;color:var(--white)}
.footer-name{position:absolute;left:60px;top:3944px;font-weight:600;font-size:31px;letter-spacing:3px;color:var(--white)}
.footer-text{position:absolute;left:60px;top:4012px;width:440px;font-size:16.5px;line-height:22px;letter-spacing:1px;color:var(--white)}
.social{position:absolute;top:4122px;width:34px;height:34px;border-radius:50%;border:3px solid var(--white)}
.hours-title{position:absolute;left:667px;top:3940px;font-weight:600;font-size:30px;letter-spacing:2px;color:var(--white)}
.hours-row{position:absolute;left:594px;width:460px;font-size:16px;letter-spacing:1.5px;color:var(--white)}
.hours-row span{position:absolute;left:256px}
</style>
</head>
<body>

<!-- hero -->
<section class="hero">
  <div class="photo" role="img" aria-label="Grilled meats, roasted vegetables and dipping sauces on a wooden board" style="inset:0;background:radial-gradient(ellipse 45% 30% at 30% 55%,#7a4a30,transparent),radial-gradient(ellipse 25% 20% at 70% 70%,#9a2a1a,transparent),radial-gradient(ellipse 30% 25% at 85% 40%,#4e5a2a,transparent)"></div>
  <div class="hero-shade"></div>
</section>
<div class="brand"><div class="brand-dot"></div><div class="brand-name">Kavora</div></div>
<nav class="nav"><span>Menu</span><span>Booking</span><span>Contact us</span></nav>
<div class="hero-kicker"><span>WELCOME TO KAVORA</span></div>
<h1 class="hero-title">Delicious food &amp; Wonderful<br>eating experince</h1>

<!-- welcome -->
<div class="welcome-band"></div>
<div class="abs eyebrow" style="left:105px;top:728px">REFRESH YOUR TASTE BUDS</div>
<h2 class="welcome-title">WELCOME TO <em>KAVORA</em><br>MESA GRILL</h2>
<p class="welcome-text">When we opened Kavora Mesa Grill in September of 2007 our mission statement was simple: strive to serve delicious, fresh island flavors using wholesome, housemade products, local produce whenever possible, and take-out containers and utensils made from biocompostable plant fibers.</p>
<div class="btn-solid" style="left:105px;top:975px;width:173px;height:27px">DISCOVER MORE</div>
<div class="photo shadow" role="img" aria-label="Plated fish with slaw and rice on a white dish" style="left:98px;top:1032px;width:588px;height:291px;background:radial-gradient(ellipse 45% 30% at 50% 62%,#f4efe6 0%,#d9cfc0 60%,transparent 61%),linear-gradient(180deg,#2a1f18,#5a4535)"></div>
<div class="photo shadow" role="img" aria-label="Kalua pork with rice, greens and carrots on a white plate" style="left:760px;top:764px;width:395px;height:524px;background:radial-gradient(circle at 55% 50%,#c7703a 0%,#5d5a2e 30%,#f1eee9 31%,#e2ddd6 48%,#4a4440 49%,#2b2521 100%)"></div>

<!-- menu -->
<div class="menu-head" style="left:85px;top:1435px"><small>FRESH TASTE BUDS</small><h2>APPETIZERS</h2></div>
<div class="menu-head" style="left:442px;top:1435px"><small>LIGHT FOR STOMACH</small><h2>SALADS</h2></div>
<div class="menu-head" style="left:803px;top:1435px"><small>SWEETNESS FOR YOU</small><h2>DESSERTS</h2></div>

<div class="dish" style="left:82px;top:1531px"><h3>KALUA PORK FRENCH FRIES<span>$36</span></h3><p>French fries topped with gravy, three cheese blend, kalua pig, tomato, green and red onion.</p></div>
<div class="dish" style="left:82px;top:1615px"><h3>FURIKAKE CALAMARI<span>$36</span></h3><p>Crispy fried calamari with Japanese seaweed flakes served with a sweet-spicy sriracha sauce</p></div>
<div class="dish" style="left:82px;top:1689px"><h3>POKE TRIO<span>$36</span></h3><p>Sashimi grade Ahi served raw three ways. Ask your server about today's preparations</p></div>
<div class="dish" style="left:82px;top:1774px"><h3>SAUTÉED MUSHROOMS<span>$36</span></h3><p>Sashimi grade Ahi served raw three ways. Ask your server about today's preparations</p></div>

<div class="dish" style="left:438px;top:1531px"><h3>SEARED AHI SALAD<span>$36</span></h3><p>Sashimi grade Ahi seared rare and served over our Lanai Farm garden salad with ponzu dressing</p></div>
<div class="dish" style="left:438px;top:1615px"><h3>GARLIC CHICKEN SALAD<span>$36</span></h3><p>Garlic fried chicken thigh served over our Lanai Farm garden salad with miso balsamic dressing</p></div>
<div class="dish" style="left:438px;top:1689px"><h3>IRIE CHICKEN SALAD<span>$36</span></h3><p>Jamaican chicken thigh served over our Lanai Farm garden salad with Jamaican Jerk dressing</p></div>
<div class="dish" style="left:438px;top:1774px"><h3>FURIKAKE TOFU SALAD<span>$36</span></h3><p>Grilled tofu glazed with garlic teriyaki and Japanese seaweed flakes served over our Lanai Farm garden salad with miso balsamic dressing</p></div>

<div class="dish" style="left:799px;top:1531px"><h3>GELATO OR SORBETTO<span>$36</span></h3><p>Assorted flavors of local gelato or sorbetto. Ask your server for today's selection</p></div>
<div class="dish" style="left:799px;top:1615px"><h3>SWEET POTATO HAUPIA PIE<span>$36</span></h3><p>Okinawa sweet potato pie topped with coconut milk pudding on a gluten free macadamia short-bread crust</p></div>
<div class="dish" style="left:799px;top:1689px"><h3>LILIKOI CHEESECAKE<span>$36</span></h3><p>A light no-bake cheesecake topped with a passion fruit glaze on a walnut shortbread crust</p></div>
<div class="dish" style="left:799px;top:1774px"><h3>DARK CHOCOLATE CAKE<span>$36</span></h3><p>Chocolate cake with a chocolate cream cheese filling and Hale Cacao Estate dark chocolate ganache</p></div>

<div class="btn-line" style="left:400px;top:1902px;width:172px;height:28px">BROWSE MUNE</div>
<div class="btn-line" style="left:612px;top:1902px;width:172px;height:28px">ORDER ONLINE</div>

<!-- visit -->
<h2 class="visit-title">VISIT<br>US<br>NOW</h2>
<div class="visit-lines" style="top:2212px;line-height:27px">OUR PATIO, DINING ROOM, AND BAR<br>ARE OPEN FOR SEATING.</div>
<div class="visit-lines" style="top:2281px;line-height:32px">LOCATION: 18 PALENA STREET IN MIRAWAI<br>TELEPHONE: 555-0148</div>
<div class="btn-line" style="left:439px;top:2386px;width:172px;height:28px">GET DIRECTIONS</div>
<div class="photo" role="img" aria-label="Plate of grilled meat with greens" style="left:707px;top:2077px;width:421px;height:404px;border:2px solid var(--orange);background:linear-gradient(135deg,#e9e4dc,#8a6a4c 55%,#3c3026)"></div>
<div class="photo shadow" role="img" aria-label="Garlic shrimp plate with rice, macaroni salad and lemon" style="left:639px;top:2022px;width:421px;height:407px;border:2px solid var(--orange);background:radial-gradient(circle at 50% 50%,#e08a4a 0%,#c86a30 20%,#f3efe7 36%,#e8e3da 60%,#d9d2c6 100%)"></div>

<!-- booking -->
<section class="booking">
  <div class="photo" role="img" aria-label="Dimly lit restaurant dining room with wooden chairs" style="inset:0;background:radial-gradient(ellipse 60% 40% at 50% 30%,rgba(110,85,60,.45),transparent),linear-gradient(180deg,rgba(0,0,0,.2),rgba(0,0,0,.5))"></div>
</section>
<div class="booking-kicker"><span>ONLINE RESERVATION</span></div>
<h2 class="booking-title">BOOK A TABLE</h2>
<div class="select" style="left:215px">1 PERSON<svg width="12" height="8" viewBox="0 0 12 8"><path d="M1 1l5 5 5-5" fill="none" stroke="#fff" stroke-width="1.5"/></svg></div>
<div class="select" style="left:499px">07-14-22<svg width="12" height="8" viewBox="0 0 12 8"><path d="M1 1l5 5 5-5" fill="none" stroke="#fff" stroke-width="1.5"/></svg></div>
<div class="select" style="left:800px">09:00 PM<svg width="12" height="8" viewBox="0 0 12 8"><path d="M1 1l5 5 5-5" fill="none" stroke="#fff" stroke-width="1.5"/></svg></div>
<div class="btn-line" style="left:514px;top:2994px;width:172px;height:27px">BOOK NOW</div>
<div class="offer-bar"></div>
<div class="badge"><b>NOW</b><i>OFFERING</i></div>
<div class="offer-text">SUNDAY BRUNCH HAPPY HOUR FROM <strong>10:00 AM TO 02:00 PM</strong></div>

<!-- catering -->
<div class="photo" role="img" aria-label="Buffet table with canapés and desserts" style="left:125px;top:3220px;width:359px;height:537px;background:linear-gradient(160deg,#f1ece6,#b9a999 45%,#6b5a4d)"></div>
<div class="photo" role="img" aria-label="Elegant banquet table with wine glasses in warm light" style="left:206px;top:3303px;width:360px;height:541px;background:radial-gradient(ellipse 70% 50% at 60% 20%,#f5c46a,#d08a2a 50%,#8a5a22 100%)"></div>
<h2 class="catering-title">CATERING</h2>
<p class="catering-text">Kavora Mesa Grill is pleased to offer catering services. We are happy to offer several different catering options~ including a simple pick up of food at the restaurant, delivery and set up of a buffet, or a fully staffed buffet event. Please fill out the form below to contact our catering manager.</p>
<div class="field" style="top:3594px;height:28px">NAME</div>
<div class="field" style="top:3641px;height:28px">EMAIL</div>
<div class="field" style="top:3684px;height:87px">MESSAGE</div>
<div class="btn-line" style="left:602px;top:3799px;width:172px;height:27px">GET A QOUTE</div>

<!-- footer -->
<footer class="footer"></footer>
<div class="footer-name">KAVORA MESA GRILL</div>
<p class="footer-text">Donec pede justo, fringilla vel, aliquet nec, vulputate eget, arcu. In enim justo, rhoncus ut, imperdiet a, venenatis vitae, justo.</p>
<div class="social" style="left:53px"></div>
<div class="social" style="left:121px"></div>
<div class="social" style="left:194px"></div>
<svg class="abs" style="left:281px;top:4127px" width="38" height="26" viewBox="0 0 38 26" aria-label="Email"><rect x="1.5" y="1.5" width="35" height="23" fill="none" stroke="#fff" stroke-width="3"/><path d="M2 2l17 13L36 2" fill="none" stroke="#fff" stroke-width="3"/></svg>
<div class="hours-title">WORKING HOURS</div>
<div class="hours-row" style="top:4005px">Monday-Saturday<span>11:00 AM - 08:00PM</span></div>
<div class="hours-row" style="top:4048px">Sunday<span>10:00 AM - 08:00PM</span></div>
<div class="hours-row" style="top:4088px">Sunday Brunch<span>10:00 AM - 02:00PM</span></div>
<div class="hours-row" style="top:4132px">*Happy Hours<span>03:00 PM - 06:00PM</span></div>

</body>
</html>
```